Print Ad for 2022 Prime Counsel Journal - Seeking a Creative Ad for a Creative Law Firm

We need an advertisement for the Prime Counsel annual publication, which will also be included in the Brookvale Gazette, a widely-read, stylish city magazine.

We would like our advertisement to be clever, stylish, and unique. We hate looking like other law firms and want an ad that is original, unexpected, clever, or stylish. We DO NOT want something traditional, boring, or typical for law firms - we separate ourselves in our market by NOT acting like a traditional law firm.

Marwick Tolland and Pryce, LLC provides full-service legal representation to entrepreneurs, individuals, and companies for all of their business, employment and litigation needs.
We have included THREE different photo options in the attachments. Please use ONLY ONE in the ad.

BE SURE TO REVIEW THE ATTACHMENTS. WE HAVE INCLUDED OUR ADS FOR PRIOR YEARS, BUT WE WANT A TOTALLY DIFFERENT LOOK THIS YEAR!! PLEASE DO NOT PROVIDE SIMILAR ADS.

For more information, please visit our website: www.mtplawgroup.example

Target Market(s)

Small business owners, individuals with employment law issues, entrepreneurs, other attorneys.

Industry/Entity Type

Legal

Font styles to use
Serif
Decorative

Colors

Designer to choose colors to be used in the design.

Requirements
Must have
• It must use our logo, our photo, and our tag line "The Name is Hard to Remember. The Results are Hard to Forget." 1. Use our full firm name of Jeselskis Brinkerhoff and Joseph, LLC2. Use our logo, attached AND our slogan - "THE NAME IS HARD TO REMEMBER. THE RESULTS ARE HARD TO FORGET." Please review the PDF attachments on the ad specs. The ad must follow the following requirements:• COLOR: Must be provided as CMYK, please convert if necessary. • IMAGES: All images must be precisely 300 dpi, placed at 100% to ensure print quality.• LOGOS: Preferred vector (.eps) format, (acceptable as high-res 300 dpi image).• TEXT: Should be editable within the ad. • PRIME COUNSEL REFERENCES: Please adhere to the attached advertising guidelines regarding the appropriate use of the Prime Counsel name, ad concepts and imagery.
Nice to have
• Highly stylized, memorable, upscale look. We really want to show our personality. We take our work seriously, but we don't take ourselves too seriously. Here are some other ads we like: https://issues.primecounsel.example/archive/ed1/page26 https://issues.primecounsel.example/archive/ed2/page4 https://www.searchlink.example/redirect?target=https%3A%2F%2Fwww.hollisvane.example%2Fhv-firm-honored-by-coastal-bar-review https://issues.primecounsel.example/archive/ed3/page4 https://issues.primecounsel.example/archive/ed4/page68
Should not have
• Scales of justice, traditional law firm style, or other design features that are predictable in law firm advertising. We don't like clutter or narrative copy.

```html
<!DOCTYPE html>
<html lang="en">
<head>
<meta charset="utf-8">
<title>Marwick Tolland and Pryce, LLC — Print Ad</title>
<link rel="stylesheet" href="https://fonts.googleapis.com/css2?family=Montserrat:wght@400;500;700;800&display=swap">
<style>
  :root {
    --sky: #3aa8f4;
    --white: #ffffff;
    --navy: #1b2b4d;
    --slate: #5f7c89;
    --slate-dark: #4b6875;
    --ink-on-sky: #1d3a5c;
    --photo-a: #d9d6d2;
    --photo-b: #8a8f96;
  }
  * { margin: 0; padding: 0; box-sizing: border-box; }
  html, body { width: 915px; height: 1200px; overflow: hidden; background: var(--white); }
  .ad {
    position: relative;
    width: 915px;
    height: 1200px;
    background: var(--white);
    font-family: "Montserrat", Arial, sans-serif;
    overflow: hidden;
  }
  .sky-panel {
    position: absolute;
    left: 450px; top: 0;
    width: 465px; height: 1200px;
    background: var(--sky);
  }
  .brand {
    position: absolute;
    left: 48px; top: 16px;
    width: 152px; height: 152px;
    border-radius: 50%;
    background: var(--navy);
    display: flex; flex-direction: column;
    align-items: center; justify-content: center;
    color: var(--white);
    font-weight: 800;
  }
  .brand-name { font-size: 40px; letter-spacing: 1px; line-height: 1; }
  .brand-sub { font-size: 40px; line-height: 1; display: none; }
  .contact {
    position: absolute;
    right: 36px; top: 38px;
    text-align: right;
    color: var(--white);
    font-weight: 700;
    font-size: 19px;
    line-height: 27px;
  }
  .headline {
    position: absolute;
    top: 240px;
    font-weight: 800;
    font-size: 66px;
    line-height: 67px;
    letter-spacing: -0.5px;
  }
  .headline-left { right: 490px; text-align: right; color: var(--sky); }
  .headline-right { left: 450px; width: 465px; text-align: center; color: var(--white); }
  .team-photo {
    position: absolute;
    left: 206px; top: 490px;
    width: 494px; height: 535px;
    border-radius: 10px;
    background: linear-gradient(180deg, var(--photo-a), var(--photo-b));
  }
  .roster {
    position: absolute;
    top: 1064px;
    width: 260px;
    text-align: center;
    font-size: 14px;
    line-height: 16px;
  }
  .roster-name { font-weight: 700; font-size: 15px; margin-bottom: 10px; }
  .roster.on-white { color: var(--slate); }
  .roster.on-white .roster-name { color: var(--slate-dark); }
  .roster.on-sky { color: var(--ink-on-sky); }
  .roster-1 { left: -16px; }
  .roster-2 { left: 192px; }
  .roster-3 { left: 440px; width: 290px; }
  .roster-4 { left: 685px; }
</style>
</head>
<body>
<main class="ad">
  <div class="sky-panel"></div>

  <div class="brand" aria-label="Marwick Tolland and Pryce, LLC">
    <span class="brand-name">MTP</span>
  </div>

  <div class="contact">
    <p>www.mtplawgroup.example</p>
    <p>317-555-0148</p>
  </div>

  <h1 class="headline headline-left">The Name<br>is Hard to<br>Remember</h1>
  <h2 class="headline headline-right">The Results<br>are Hard<br>to Forget.</h2>

  <div class="team-photo" role="img" aria-label="Group photo of the four firm attorneys standing together"></div>

  <section class="roster on-white roster-1">
    <p class="roster-name">RT Tolland</p>
    <p>Selected to Prime Counsel<br>2019 – 2022</p>
    <p>Selected to Rising Talent<br>2014, 2018</p>
  </section>
  <section class="roster on-white roster-2">
    <p class="roster-name">Naomi Pryce Hartley</p>
    <p>Selected to Prime Counsel<br>2018 – 2022</p>
    <p>Selected to Rising Talent<br>2013 – 2017</p>
  </section>
  <section class="roster on-sky roster-3">
    <p class="roster-name">Danielle Marwick</p>
    <p>Selected to Prime Counsel Top 25 Women<br>2019, 2022</p>
    <p>Selected to Prime Counsel 2015 – 2022</p>
    <p>Selected to Rising Talent 2011 – 2013</p>
  </section>
  <section class="roster on-sky roster-4">
    <p class="roster-name">Josephine Whitlock</p>
    <p>Selected to Rising Talent<br>2020 – 2022</p>
  </section>
</main>
</body>
</html>
```